New corporate e-mail signature

We need a new e-mail signature for our company that is clean and professional. The requests are attached in a document.

Target Market(s)

CFO, CTO, Controllers, leaders, decision-makers.

Industry/Entity Type

Information Technology

Colors

Designer to choose colors to be used in the design.

Requirements
Must have
• See the PowerPoint document.
• - keep it as simple as possible.
• - same style as our new website design
• - It has to look good in all e-mail readers, and on all surfaces.
Nice to have
• - Please also attach 'best practise' for how to use the signature.
Should not have
• See the PowerPoint document. Use our color palette.
• - Do not include photo!

```html
<!DOCTYPE html>
<html lang="en">
<head>
<meta charset="utf-8">
<title>Northbeam Metals – Email Signature</title>
<link rel="stylesheet" href="https://fonts.googleapis.com/css2?family=Roboto:wght@400;500&display=swap">
<style>
  :root {
    --navy: #0b3868;
    --panel: #f7f7f7;
    --ground: #e6d8c4;
    --muted: #6b6b6b;
    --white: #ffffff;
  }
  * { margin: 0; padding: 0; box-sizing: border-box; }
  html, body {
    width: 1200px;
    height: 600px;
    overflow: hidden;
  }
  body {
    background: var(--ground);
    font-family: "Roboto", Arial, sans-serif;
    position: relative;
  }
  .signature {
    position: absolute;
    left: 55px;
    top: 135px;
    width: 1091px;
    height: 330px;
    background: var(--panel);
    box-shadow: 0 2px 6px rgba(0,0,0,0.12);
  }
  .brand-panel {
    position: absolute;
    left: 0;
    top: 0;
    width: 330px;
    height: 330px;
    background: var(--navy);
    display: flex;
    flex-direction: column;
    align-items: center;
    justify-content: center;
    gap: 26px;
  }
  .brand-mark {
    width: 64px;
    height: 64px;
    background: var(--white);
  }
  .brand-name {
    color: var(--white);
    font-size: 26px;
    font-weight: 400;
    letter-spacing: 0.2px;
  }
  .identity {
    position: absolute;
    left: 366px;
    top: 40px;
    color: var(--navy);
  }
  .identity .person-name {
    font-size: 31px;
    font-weight: 500;
    line-height: 36px;
  }
  .identity .job-title {
    font-size: 22px;
    font-weight: 400;
    line-height: 30px;
  }
  .contact-list {
    position: absolute;
    left: 364px;
    top: 127px;
    list-style: none;
  }
  .contact-item {
    display: flex;
    align-items: center;
    height: 28px;
    margin-bottom: 15px;
    color: var(--muted);
    font-size: 20px;
  }
  .contact-icon {
    width: 28px;
    height: 28px;
    margin-right: 16px;
    flex: none;
  }
  .social-links {
    position: absolute;
    left: 991px;
    top: 41px;
    list-style: none;
  }
  .social-link {
    width: 52px;
    height: 52px;
    margin-bottom: 13px;
    background: var(--navy);
    border-radius: 6px;
    color: var(--white);
    font-size: 16px;
    font-weight: 500;
    display: flex;
    align-items: center;
    justify-content: center;
  }
</style>
</head>
<body>
  <section class="signature">
    <div class="brand-panel">
      <div class="brand-mark"></div>
      <div class="brand-name">NORTHBEAM METALS</div>
    </div>

    <div class="identity">
      <div class="person-name">Maren Holloway</div>
      <div class="job-title">Steel Co-ordinator</div>
    </div>

    <ul class="contact-list">
      <li class="contact-item">
        <svg class="contact-icon" viewBox="0 0 28 28" aria-hidden="true">
          <rect x="1" y="1" width="26" height="26" rx="4" fill="none" stroke="#0b3868" stroke-width="2"/>
          <path d="M6 12 L14 7 L22 12 V21 H6 Z" fill="#0b3868"/>
          <path d="M6 12 L14 17 L22 12" fill="none" stroke="#ffffff" stroke-width="1.5"/>
        </svg>
        mholloway@nbmetals.com
      </li>
      <li class="contact-item">
        <svg class="contact-icon" viewBox="0 0 28 28" aria-hidden="true">
          <rect x="1" y="1" width="26" height="26" rx="4" fill="none" stroke="#0b3868" stroke-width="2"/>
          <path d="M9 7 L12 7 L13 11 L11 12.5 C12 15 13 16 15.5 17 L17 15 L21 16 L21 19 C21 20 20 21 19 21 C13 20 8 15 7 9 C7 8 8 7 9 7 Z" fill="#0b3868"/>
        </svg>
        +1 (555) 014201
      </li>
      <li class="contact-item">
        <svg class="contact-icon" viewBox="0 0 28 28" aria-hidden="true">
          <rect x="1" y="1" width="26" height="26" rx="4" fill="none" stroke="#0b3868" stroke-width="2"/>
          <rect x="10" y="6" width="8" height="16" rx="1.5" fill="none" stroke="#0b3868" stroke-width="2"/>
          <line x1="13" y1="19" x2="15" y2="19" stroke="#0b3868" stroke-width="1.5"/>
        </svg>
        +1 (555) 014202
      </li>
      <li class="contact-item">
        <svg class="contact-icon" viewBox="0 0 28 28" aria-hidden="true">
          <rect x="1" y="1" width="26" height="26" rx="4" fill="none" stroke="#0b3868" stroke-width="2"/>
          <path d="M14 6 C10.5 6 8 8.5 8 12 C8 16 14 22 14 22 C14 22 20 16 20 12 C20 8.5 17.5 6 14 6 Z" fill="#0b3868"/>
          <circle cx="14" cy="12" r="2.3" fill="#ffffff"/>
        </svg>
        Ground Floor, 48 Harbour Lane, Eastport WA 6100
      </li>
    </ul>

    <ul class="social-links">
      <li class="social-link">Pal</li>
      <li class="social-link">Net</li>
      <li class="social-link">Orb</li>
      <li class="social-link">Tik</li>
    </ul>
  </section>
</body>
</html>
```